brindlewood carpentry business card 2.0

id like to get some extra info added to my current business card ,but i am also open to a new design as well ,id like it to be a clean professional look
i have attached the original card files, i have also attached the ridgemark guild logo and licensed builder logo that id like to add to all the current info on the old card
also the color green is important as seen in the company logo

Industry/Entity Type

Carpentry

Colors
9bcb3c

```html
<!DOCTYPE html>
<html lang="en">
<head>
<meta charset="utf-8">
<title>Brindlewood Carpentry – Business Card</title>
<link rel="stylesheet" href="https://fonts.googleapis.com/css2?family=Montserrat:wght@400;500;600&display=swap">
<style>
  :root {
    --brand-green: #9bcb3c;
    --paper: #ffffff;
    --ink: #3a3a3a;
    --backdrop: #dcfbe0;
    --badge-blue: #1f3f8f;
  }
  * { margin: 0; padding: 0; box-sizing: border-box; }
  html, body { width: 1200px; height: 1132px; overflow: hidden; }
  body {
    background: var(--backdrop);
    font-family: "Montserrat", Arial, sans-serif;
    position: relative;
  }
  .card {
    position: absolute;
    left: 180px;
    width: 840px;
    height: 524px;
    overflow: hidden;
  }
  .card--front { top: 28px; background: var(--brand-green); }
  .card--back  { top: 580px; background: var(--paper); }

  .front-wordmark {
    position: absolute;
    inset: 0;
    display: flex;
    flex-direction: column;
    align-items: center;
    justify-content: center;
    color: var(--paper);
    font-weight: 400;
    letter-spacing: 2px;
    line-height: 1.05;
    text-align: center;
  }
  .front-wordmark .name-main { font-size: 72px; }
  .front-wordmark .name-sub { font-size: 40px; letter-spacing: 4px; }

  .back-wordmark {
    position: absolute;
    left: 40px;
    top: 200px;
    width: 340px;
    text-align: center;
    color: var(--ink);
    font-weight: 400;
    line-height: 1.1;
  }
  .back-wordmark .name-main { font-size: 38px; letter-spacing: 1px; }
  .back-wordmark .name-sub { font-size: 22px; letter-spacing: 3px; }

  .badge { position: absolute; }
  .badge--guild {
    left: 102px; top: 372px;
    width: 52px; height: 66px;
    background: var(--badge-blue);
  }
  .badge--registry {
    left: 266px; top: 372px;
    width: 68px; height: 68px;
    border-radius: 50%;
    background: var(--brand-green);
  }

  .contact-panel {
    position: absolute;
    left: 420px;
    top: 48px;
    width: 420px;
    height: 428px;
    background: var(--brand-green);
    color: var(--paper);
    padding: 92px 24px 0 44px;
  }
  .contact-name { font-size: 36px; font-weight: 600; line-height: 1; }
  .contact-role { font-size: 17px; font-weight: 500; margin-top: 14px; letter-spacing: .2px; white-space: nowrap; }
  .contact-list { list-style: none; margin-top: 30px; }
  .contact-list li {
    display: flex;
    align-items: center;
    gap: 18px;
    font-size: 15px;
    font-weight: 500;
    height: 48px;
    white-space: nowrap;
  }
  .contact-list svg { width: 22px; height: 22px; flex: none; }
</style>
</head>
<body>
  <section class="card card--front" aria-label="Business card front">
    <div class="front-wordmark">
      <span class="name-main">BRINDLEWOOD</span>
      <span class="name-sub">CARPENTRY</span>
    </div>
  </section>

  <section class="card card--back" aria-label="Business card back">
    <div class="back-wordmark">
      <div class="name-main">BRINDLEWOOD</div>
      <div class="name-sub">CARPENTRY</div>
    </div>
    <div class="badge badge--guild" role="img" aria-label="Ridgemark Guild membership badge"></div>
    <div class="badge badge--registry" role="img" aria-label="Stonegate Trade Registry badge"></div>

    <div class="contact-panel">
      <div class="contact-name">Marcus Keller</div>
      <div class="contact-role">director Brindlewood Carpentry Ltd</div>
      <ul class="contact-list">
        <li>
          <svg viewBox="0 0 24 24" aria-hidden="true"><path fill="#fff" d="M6.6 10.8a15.1 15.1 0 0 0 6.6 6.6l2.2-2.2c.3-.3.7-.4 1-.2 1.1.4 2.3.6 3.6.6.6 0 1 .4 1 1V20c0 .6-.4 1-1 1A17 17 0 0 1 3 4c0-.6.4-1 1-1h3.5c.6 0 1 .4 1 1 0 1.3.2 2.5.6 3.6.1.3 0 .7-.2 1z"/></svg>
          <span>02109876543</span>
        </li>
        <li>
          <svg viewBox="0 0 24 24" aria-hidden="true"><path fill="#fff" d="M2 6h20v12H2z"/><path fill="none" stroke="#9bcb3c" stroke-width="1.8" d="M2.5 6.5 12 13l9.5-6.5"/></svg>
          <span>marcus@brindlewoodcarpentry.co.nz</span>
        </li>
        <li>
          <svg viewBox="0 0 24 24" aria-hidden="true"><g fill="none" stroke="#fff" stroke-width="1.6"><circle cx="12" cy="12" r="9"/><ellipse cx="12" cy="12" rx="4" ry="9"/><path d="M3 12h18M4.5 7.5h15M4.5 16.5h15"/></g></svg>
          <span>www.brindlewoodcarpentry.co.nz</span>
        </li>
      </ul>
    </div>
  </section>
</body>
</html>
```